Online Digital Solutions Agency needs a New Business Card

We are a Online/Digital solution agency. We provide WordPress Solutions, Online & Digital Marketing Solutions including SEO, Social Media Marketing and Managed Hosting including VPS and Cloud Hosting solutions. We also design and build bespoke web sites and web applications for various clients. We are very good at site migrations, 3rd party API integrations and mobile app development.

We are rebranding our agency and have already designed a new logo. We have selected 5-6 colours as our base colour and are currently building our new website based around these colour scheme.

Our logo indicates that we are a cloud solution providers, and (i.e. the Clouds), and developers (i.e. HTML Tags, and CSS formats). We use the 5-6 base colours and use various shades of these colours as required.

Our old website is located at: www.brindleharbour.com

And our new website is going to be at (we are working on it at the moment ...):
https://creative.brindleharbour.co.uk/

Our slogan is "Digital Transformation Specialist"

What we mean by that is; we can take any existing business and get them up and transform them in to the digital world, starting with Hosting, Web Design, Development & Online Marketing aspects.

The powerpoint is a document that we use to present our projects to clients at the moment, and the cloud is on the background as we clarified earlier. (Just to get the idea)

What we are looking for is a Great WoW factor design to start with, ideally with the Logo and Logo colour scheme if possible but not required as long as the designers can do better, and basically give life to our logo and company via the Business card design.

Ideally with some icons perhaps to indicate the address, location, mobile, email, and website would be good but again optional as long as there is a good design.

The cloud can be used as a background if required in a light shade or as a watermark share perhaps.

The logos' and the Illustrator files are shared with you so you can use them as required.

Ideally the business card should have a Name, title, Mobile, Email , Website, Address and perhaps some social media links.

Target Market(s)

New Startups, SME's, Contract and Outsource Clients

Contact Information for Business Card

Company Name:
==============
Brindle Harbour (UK) Ltd.

Tag Line:
========
“Digital Transformation Specialists”

Adress:
=======

Suite QR73520
14-16 Marrowby Street
London
E9 4KD.

Name:
=====
Odric Pellan

Title: (Optional)
=============
MSc, BEng (Hons)

Role:
=====
Cloud Platform Lead

Email:
=====
odric@brindleharbour.uk

WebSite:
=======
http://www.brindleharbour.uk

OR

www.brindleharbour.uk

Mobile:
======
0044 (0)75 318 20473

OR

+44 (0)75 318 20473

LinkedIN: (Optional)
========
https://uk.linkedin.com/in/odricpellan

Skype: (Optional)
======
odric.pellan

Twitter (Optional) : odricpellan

Font styles to use
Serif
Sans Serif

Requirements
Must have
• The Logo
• Business Name
• Person Name
• Title
• Mobile
• Email
• Website
• Address
• I have provided the colour scheme on my files.
Nice to have
• Twiter
• Linked in
• Facebook

```html
<!DOCTYPE html>
<html lang="en">
<head>
<meta charset="utf-8">
<title>Brindle Harbour – Business Card</title>
<link rel="stylesheet" href="https://fonts.googleapis.com/css2?family=Arimo:wght@400;700&display=swap">
<style>
  :root {
    --stage: #2b2b2d;
    --sun: #f8b72c;
    --sun-deep: #f3a91f;
    --navy: #0f5aa8;
    --blue-top: #0b6fc2;
    --blue-bottom: #4fd4f6;
    --sky: #7fd9f5;
    --white: #ffffff;
    --accent: #f29b12;
  }
  * { box-sizing: border-box; margin: 0; padding: 0; }
  html, body { width: 1200px; height: 892px; overflow: hidden; }
  body {
    background: var(--stage);
    font-family: "Arimo", Arial, sans-serif;
    position: relative;
  }
  .card {
    position: absolute;
    width: 540px;
    height: 308px;
    border-radius: 22px;
    overflow: hidden;
  }
  .card-front {
    left: 70px; top: 110px;
    background: linear-gradient(160deg, var(--sun) 0%, var(--sun-deep) 100%);
    display: flex; align-items: center; justify-content: center; gap: 14px;
  }
  .brand-dot {
    width: 30px; height: 30px; border-radius: 50%;
    background: var(--navy);
  }
  .brand-name-front {
    color: var(--navy);
    font-weight: 700;
    font-size: 40px;
    letter-spacing: 0.5px;
  }
  .card-back {
    left: 590px; top: 474px;
    background: linear-gradient(165deg, var(--blue-top) 0%, #2aa4de 55%, var(--blue-bottom) 100%);
    color: var(--white);
  }
  .back-panel { position: absolute; inset: 0; }
  .person { position: absolute; left: 34px; top: 44px; }
  .person-name { font-size: 25px; font-weight: 400; margin-bottom: 6px; }
  .person-role { font-size: 15px; line-height: 1.3; }
  .address {
    position: absolute; left: 34px; top: 156px;
    font-size: 14px; line-height: 1.3;
  }
  .contact-list {
    position: absolute; left: 34px; top: 220px;
    list-style: none; font-size: 14px; line-height: 1.35;
  }
  .contact-list li { display: flex; align-items: center; gap: 8px; }
  .contact-list svg { width: 13px; height: 13px; flex: none; }
  .brand-block {
    position: absolute; right: 12px; top: 110px;
    width: 206px; text-align: center;
  }
  .brand-name-back {
    color: var(--navy); font-weight: 700; font-size: 24px; line-height: 1.05;
    white-space: nowrap;
  }
  .tagline {
    margin-top: 8px; color: var(--accent); font-size: 10px; font-weight: 700;
    letter-spacing: 0.3px; white-space: nowrap;
  }
  .handles {
    margin-top: 12px; color: var(--navy); font-size: 12.5px;
    display: flex; justify-content: center; gap: 16px;
  }
</style>
</head>
<body>
  <section class="card card-front" aria-label="Card front">
    <span class="brand-dot"></span>
    <span class="brand-name-front">Brindle Harbour</span>
  </section>

  <section class="card card-back" aria-label="Card back">
    <svg class="back-panel" viewBox="0 0 540 308" preserveAspectRatio="none" aria-hidden="true">
      <ellipse cx="470" cy="160" rx="200" ry="200" fill="var(--sky)" opacity="0.45"/>
      <ellipse cx="485" cy="165" rx="180" ry="185" fill="var(--white)"/>
    </svg>

    <div class="person">
      <p class="person-name">Odric Pellan</p>
      <p class="person-role">MSc, BEng (Hons)<br>Cloud Platform Lead</p>
    </div>

    <p class="address">14-16 Marrowby Street<br>London, E9 4KD<br>United Kingdom</p>

    <ul class="contact-list">
      <li>
        <svg viewBox="0 0 14 14"><rect x="3.5" y="0.8" width="7" height="12.4" rx="1.4" fill="none" stroke="#fff" stroke-width="1.4"/><circle cx="7" cy="11" r="0.8" fill="#fff"/></svg>
        +44 (0)75 318 20473
      </li>
      <li>
        <svg viewBox="0 0 14 14"><rect x="0.8" y="2.5" width="12.4" height="9" rx="1" fill="none" stroke="#fff" stroke-width="1.4"/><path d="M1 3l6 5 6-5" fill="none" stroke="#fff" stroke-width="1.4"/></svg>
        odric@brindleharbour.uk
      </li>
      <li>
        <svg viewBox="0 0 14 14"><circle cx="7" cy="7" r="6" fill="none" stroke="#fff" stroke-width="1.3"/><ellipse cx="7" cy="7" rx="2.6" ry="6" fill="none" stroke="#fff" stroke-width="1.1"/><path d="M1 7h12" stroke="#fff" stroke-width="1.1"/></svg>
        www.brindleharbour.uk
      </li>
    </ul>

    <div class="brand-block">
      <p class="brand-name-back">Brindle Harbour</p>
      <p class="tagline">WEB &amp; CLOUD DELIVERY EXPERTS</p>
      <p class="handles"><span>odricpellan</span><span>odric.pellan</span></p>
    </div>
  </section>
</body>
</html>
```